Letterhead design for business

Looking for an attractive and professional letterhead that uses the logo that is attached below.

Target Market(s)

Potential bankruptcy clients.

Industry/Entity Type

Legal

Colors

Designer to choose colors to be used in the design.

Requirements
Must have
• Address for locations, phone number, and website address.
• Addresses are on website larkmoorfirm.legal. Use following phone number (for tracking purposes): 404-731-2864

```html
<!DOCTYPE html>
<html lang="en">
<head>
<meta charset="utf-8">
<title>Larkmoor Law Group Letterhead</title>
<link rel="stylesheet" href="https://fonts.googleapis.com/css2?family=Roboto:wght@400;500&family=Dosis:wght@500&display=swap">
<style>
  :root {
    --backdrop: #2f2f30;
    --paper: #ffffff;
    --header-dark: #3b3b3c;
    --brand-green: #6fbf7a;
    --ink: #6a6a6a;
    --ink-dark: #444444;
    --rule: #9a9a9a;
  }
  html, body {
    margin: 0;
    padding: 0;
    width: 1200px;
    height: 946px;
    overflow: hidden;
    background: var(--backdrop);
  }
  .canvas {
    position: relative;
    width: 1200px;
    height: 946px;
  }
  .letterhead {
    position: absolute;
    left: 287px;
    top: 33px;
    width: 654px;
    height: 920px;
    background: var(--paper);
    transform: scale(0.957);
    transform-origin: 0 0;
    font-family: "Roboto", Arial, sans-serif;
    color: var(--ink);
    box-shadow: 0 6px 24px rgba(0,0,0,0.45);
  }
  .header-band {
    position: absolute;
    left: 0;
    top: 0;
    width: 654px;
    height: 170px;
    display: block;
  }
  .brand {
    position: absolute;
    left: 51px;
    top: 91px;
    display: flex;
    align-items: center;
    gap: 12px;
  }
  .brand-dot {
    width: 46px;
    height: 46px;
    border-radius: 50%;
    background: var(--brand-green);
  }
  .brand-divider {
    width: 2px;
    height: 74px;
    background: var(--brand-green);
  }
  .brand-name {
    font-family: "Dosis", "Roboto", sans-serif;
    font-weight: 500;
    font-size: 28px;
    line-height: 1.1;
    color: var(--ink-dark);
    letter-spacing: 0.5px;
  }
  .brand-name small {
    display: block;
    font-size: 12px;
    letter-spacing: 2.5px;
    margin-top: 2px;
  }
  .recipient {
    position: absolute;
    left: 53px;
    top: 278px;
    font-size: 12px;
    line-height: 17px;
    margin: 0;
  }
  .body-copy {
    position: absolute;
    left: 53px;
    width: 544px;
    margin: 0;
    font-size: 11.4px;
    line-height: 17px;
    text-align: justify;
  }
  .body-copy.first { top: 380px; }
  .body-copy.second { top: 534px; }
  .signature {
    position: absolute;
    left: 53px;
    top: 626px;
    width: 126px;
    height: 82px;
    background: linear-gradient(135deg, rgba(111,191,122,0.25), rgba(111,191,122,0.08));
  }
  .sign-title {
    position: absolute;
    left: 52px;
    top: 724px;
    font-size: 12px;
    margin: 0;
  }
  .footer {
    position: absolute;
    left: 54px;
    top: 848px;
    width: 384px;
    font-size: 10.5px;
    color: var(--ink-dark);
  }
  .footer-address {
    padding-bottom: 5px;
    border-bottom: 1px solid var(--rule);
  }
  .footer-contacts {
    display: flex;
    align-items: center;
    gap: 10px;
    margin-top: 8px;
    white-space: nowrap;
  }
  .footer-contacts .sep { color: var(--rule); }
  .footer-contacts .item { display: flex; align-items: center; gap: 5px; }
  .footer-contacts svg { width: 10px; height: 10px; fill: var(--brand-green); }
</style>
</head>
<body>
<div class="canvas">
  <article class="letterhead">
    <svg class="header-band" viewBox="0 0 654 170" aria-hidden="true">
      <path d="M0 0 H654 V164 C520 110 340 40 180 44 C90 46 30 60 0 72 Z" fill="var(--header-dark)"/>
      <path d="M20 66 C120 36 260 38 380 66 C480 88 580 130 654 164 L654 158 C580 122 480 80 380 58 C260 32 120 34 20 66 Z" fill="var(--brand-green)"/>
    </svg>

    <div class="brand">
      <span class="brand-dot"></span>
      <span class="brand-divider"></span>
      <div class="brand-name">Larkmoor<small>LAW GROUP</small></div>
    </div>

    <p class="recipient">Dear Halvorsen<br>Norbeck Print Works Corporation<br>Department Design</p>

    <p class="body-copy first">Lorem ipsum dolor sit amet, consectetuer adipiscing elit. Aenean commodo ligula eget dolor. Aenean massa. Cum sociis natoque penatibus et magnis dis parturient montes, nascetur ridiculus mus. Donec quam felis, ultricies nec, pellentesque eu, pretium quis, sem. Nulla consequat massa quis enim. Donec pede justo, fringilla vel, aliquet nec, vulputate eget, arcu. In enim justo, rhoncus ut, imperdiet a, venenatis vitae, justo. Nullam dictum felis eu pede mollis pretium. Integer tincidunt. Cras dapibus. Vivamus elementum semper nisi.Nullam dictum felis eu pede mollis pretium. Integer tincidunt. Cras dapibus. Vivamus elementum semper nisi.felis eu pede mollis pretium. Integer tincidunt. Cras dapibus.</p>

    <p class="body-copy second">Quisque rutrum. Aenean imperdiet. Etiam ultricies nisi vel augue. Curabitur ullamcorper ultricies nisi. Nam eget dui. Etiam rhoncus. Maecenas tempus, tellus eget condimentum rhoncus, sem quam semper libero, sit amet adipiscing sem neque sed ipsum.felis pede mollis pretium. I am tincidunt. Cras dapibus.</p>

    <div class="signature" role="img" aria-label="Handwritten signature of the director"></div>
    <p class="sign-title">Director/Excecutive Director</p>

    <footer class="footer">
      <div class="footer-address">Level 5, 210 Harlow Street, Brookvale, VIC 3090</div>
      <div class="footer-contacts">
        <span class="item">
          <svg viewBox="0 0 10 10"><path d="M2 0.5 L3.6 0.5 L4.3 2.8 L3.2 3.7 C3.8 5 4.9 6.1 6.3 6.8 L7.2 5.7 L9.5 6.4 L9.5 8 C9.5 9 8.8 9.5 8 9.5 C4 9.2 0.8 6 0.5 2 C0.5 1.2 1 0.5 2 0.5 Z"/></svg>
          404-731-2864
        </span>
        <span class="sep">|</span>
        <span class="item">
          <svg viewBox="0 0 10 10"><path d="M0.5 2 H9.5 V8.5 H0.5 Z M0.5 2 L5 5.5 L9.5 2" stroke="#fff" stroke-width="0.8"/></svg>
          info@larkmoorfirm.legal
        </span>
        <span class="sep">|</span>
        <span class="item">
          <svg viewBox="0 0 10 10"><circle cx="5" cy="5" r="4.5"/><path d="M0.5 5 H9.5 M5 0.5 C3 3 3 7 5 9.5 M5 0.5 C7 3 7 7 5 9.5" stroke="#fff" stroke-width="0.6" fill="none"/></svg>
          www.larkmoorfirm.legal
        </span>
      </div>
    </footer>
  </article>
</div>
</body>
</html>
```